Alternative Health Practice - Website redesign

With regard to the welcome image, stock photos can't show the faces of other people. And please don't submit a design for a one-page website.
Hello, I am redesigning a website and need some help from a professional.
The old website is here: peter-lindqvist.net (pls note I don't want to reuse the welcome photo from the old site). Much of the written content will remain the same, so note that I also need a page layout/text colour etc that works for text heavy pages: ie www.peter-lindqvist.net/somatic-articles and www.peter-lindqvist.net/client-reviews
My effort at redesigning is underway here: https://pjlindqvist.sitebuilderhost.net/my-site-7
The original sitebuilder template is this one: https://www.sitebuilderhost.net/website-template/view/html/4917?originUrl=https%3A%2F%2Fwww.sitebuilderhost.net%2Fwebsite%2Ftemplates%2Fhtml%2Fhealth-wellness&tpClick=view_button&esi=8a41c27d-03e9-4c6b-b1f2-9d5e02a7c4f3
I'm pretty happy with the colour palette. My name Peter Joseph Lindqvist is now the "brand" without Rooted Stillness subtitle. Regarding the Welcome section, if you are going to use my photos, it probably needs to be those two that are already there. If you want to put a stock photo there instead, that's fine.
If you want to propose something quite different to my design, I'm happy to receive design files in Photoshop or whatever and then subsequently replicate on Sitebuilder. Up to you.
Mostly women, some men ages 28-60.

```html
<!DOCTYPE html>
<html lang="en">
<head>
<meta charset="utf-8">
<title>Peter Lindqvist — Somatic Practice</title>
<link href="https://fonts.googleapis.com/css2?family=Lato:wght@400;700;900&display=swap" rel="stylesheet">
<style>
:root{
  --gold:#9a7230;
  --gold-dark:#7d5b22;
  --ink:#1f1a17;
  --muted:#5d554f;
  --beige:#ecdfcb;
  --beige-line:#d9c6a6;
  --hero-a:#f6e9ea;
  --hero-b:#ead9c5;
  --dark:#2a221d;
  --footer:#2e2621;
  --white:#ffffff;
  --star:#e4a92a;
}
*{box-sizing:border-box;margin:0;padding:0}
html,body{width:1200px;height:3048px;overflow:hidden}
body{font-family:'Lato',sans-serif;color:var(--ink);background:var(--white);position:relative}
.btn{display:inline-block;background:var(--gold);color:var(--white);font-size:12px;font-weight:700;padding:11px 22px;border-radius:22px}
.section-label{font-size:20px;color:var(--muted);font-weight:400}
.section-title{font-size:30px;font-weight:700;color:var(--ink)}
.ph{position:absolute}

/* header */
.site-header{position:absolute;left:0;top:0;width:1200px;height:70px;background:var(--dark);display:flex;align-items:center;padding:0 60px;z-index:2}
.brand{display:flex;align-items:center;gap:10px;color:var(--white);font-size:17px;font-weight:700;letter-spacing:2px}
.brand-dot{width:14px;height:14px;border-radius:50%;background:var(--gold)}
.main-nav{display:flex;gap:34px;margin-left:226px;font-size:12px;color:#d8cfc6}
.main-nav .active{color:var(--white);font-weight:700}
.site-header .btn{margin-left:auto;font-size:11px;padding:10px 20px}

/* hero */
.hero{position:absolute;top:0;left:0;width:1200px;height:660px;background:linear-gradient(100deg,var(--hero-a),var(--hero-b))}
.hero-badge{position:absolute;left:60px;top:196px;font-size:14px;font-weight:700;display:flex;align-items:center;gap:8px}
.hero-badge i{width:16px;height:12px;background:#3a8c4a;border-radius:2px;display:block}
.hero h1{position:absolute;left:60px;top:224px;font-size:46px;line-height:56px;font-weight:900}
.hero-inline{display:inline-block;width:44px;height:44px;border-radius:50%;vertical-align:-6px;background:linear-gradient(135deg,#c9a98a,#8a6a55)}
.hero h2{position:absolute;left:60px;top:372px;font-size:34px;font-weight:700}
.hero p{position:absolute;left:60px;top:428px;width:380px;font-size:12px;line-height:18px;color:var(--muted)}
.hero .btn{position:absolute;left:60px;top:502px}
.hero-photo{left:606px;top:130px;width:534px;height:452px;border-radius:6px;background:linear-gradient(135deg,#d8c9bb,#b8957a 55%,#6e5a4c)}

/* about */
.about{position:absolute;top:660px;left:0;width:1200px;height:640px}
.about-portrait{left:128px;top:180px;width:200px;height:290px;border-radius:100px 100px 8px 8px;background:linear-gradient(160deg,#c7b19a,#8b7462)}
.about-side{left:372px;top:180px;width:250px;height:170px;border-radius:6px;background:linear-gradient(135deg,#e6e6e3,#8f8f8c)}
.about-text{position:absolute;left:668px;top:82px;width:470px}
.about-text .section-label{display:block;margin-bottom:10px}
.about-text h3{font-size:28px;line-height:34px;font-weight:700;margin-bottom:14px}
.about-text p{font-size:12px;line-height:18px;color:var(--muted)}
.stats{display:flex;gap:64px;margin:30px 0 26px}
.stat b{display:block;font-size:32px;font-weight:700}
.stat b.gold{color:var(--gold)}
.stat span{font-size:12px}

/* services */
.services{position:absolute;top:1300px;left:0;width:1200px;height:390px;text-align:center}
.services .section-label{position:absolute;left:0;right:0;top:54px}
.services .section-title{position:absolute;left:0;right:0;top:88px}
.cards{position:absolute;left:60px;top:150px;display:flex;gap:28px}
.card{width:340px;height:180px;border-radius:10px;background:var(--beige);padding:20px 30px;display:flex;flex-direction:column;align-items:center}
.card.light{background:var(--white);border:1px solid var(--beige-line)}
.card svg{margin-bottom:6px}
.card h4{font-size:15px;font-weight:700;margin-bottom:10px}
.card p{font-size:11px;line-height:16px;color:var(--muted);width:240px}
.card .btn{margin-top:12px;padding:7px 18px;font-size:10px}

/* reviews */
.reviews{position:absolute;top:1690px;left:0;width:1200px;height:350px}
.reviews .section-label{position:absolute;left:64px;top:38px}
.reviews .section-title{position:absolute;left:64px;top:72px}
.review-row{position:absolute;left:64px;top:168px;display:flex;gap:30px}
.review{width:520px;height:122px;background:var(--beige);border-radius:60px 12px 12px 60px;padding:14px 22px 14px 14px;display:flex;gap:18px;align-items:center}
.review-avatar{width:92px;height:92px;border-radius:50%;background:linear-gradient(135deg,#c9a27a,#6b4d3a);flex:none}
.review-body{flex:1}
.review-head{display:flex;justify-content:space-between;align-items:center;margin-bottom:8px}
.review-head b{font-size:14px}
.stars{color:var(--star);font-size:15px;letter-spacing:2px}
.review p{font-size:11px;line-height:16px;color:var(--muted)}

/* contact */
.contact{position:absolute;top:2040px;left:0;width:1200px;height:520px}
.contact-form{position:absolute;left:176px;top:42px;width:440px}
.field{height:42px;border:1px solid #9a9490;border-radius:8px;font-size:12px;color:var(--muted);padding:13px 16px;margin-bottom:16px;box-shadow:0 3px 6px rgba(0,0,0,.12)}
.field.tall{height:112px}
.contact-info{position:absolute;left:656px;top:78px;width:380px}
.contact-info h3{font-size:24px;font-weight:400;margin-bottom:16px}
.contact-info h4{font-size:22px;font-weight:400;margin-bottom:24px;line-height:30px}
.info-line{display:flex;align-items:center;gap:12px;font-size:12px;margin-bottom:20px}
.social{display:flex;align-items:center;gap:8px;font-size:10px;margin-bottom:24px}
.social i{width:10px;height:10px;border-radius:50%;background:var(--ink);display:block}
.contact-info .btn{width:212px;text-align:center}

/* footer */
.site-footer{position:absolute;top:2560px;left:0;width:1200px;height:488px;background:linear-gradient(120deg,#3a302a,var(--footer) 45%,#4a3d33);color:var(--white)}
.footer-brand{position:absolute;left:58px;top:110px;display:flex;align-items:center;gap:12px;font-size:22px;font-weight:700;letter-spacing:2px}
.footer-brand i{width:26px;height:26px;border-radius:50%;background:var(--gold);display:block}
.footer-social{position:absolute;left:58px;top:160px;display:flex;gap:10px}
.footer-social i{width:14px;height:14px;border-radius:3px;background:var(--white);display:block}
.footer-col{position:absolute;top:80px;font-size:12px;line-height:34px;color:#e7ddd3}
.footer-col h5{font-size:16px;font-weight:400;color:var(--white);line-height:24px;margin-bottom:8px}
.footer-note{position:absolute;left:800px;top:80px;width:110px;font-size:11px;line-height:17px;color:#e7ddd3}
.footer-rule{position:absolute;left:0;right:0;top:398px;height:1px;background:rgba(255,255,255,.35)}
.copyright{position:absolute;left:0;right:0;top:436px;text-align:center;font-size:13px;font-weight:700}
</style>
</head>
<body>

<section class="hero">
  <div class="hero-badge"><i></i>Trauma-Informed Certified Practitioner</div>
  <h1>Healing Through <span class="hero-inline" role="img" aria-label="Small round photo of a hands-on session"></span><br>Body Awareness.</h1>
  <h2>Come Home to Your Body</h2>
  <p>Lorem ipsum dolor sit amet, consectetur adipiscing elit, sed do eiusmod tempor incididunt ut labore et dolore magna aliqua. Ut enim ad minim veniam, quis nostrud exercitation ullamco laboris.</p>
  <span class="btn">See What Clients Say</span>
  <div class="ph hero-photo" role="img" aria-label="Photo of a practitioner's hands gently supporting a client's head during a session"></div>
</section>

<header class="site-header">
  <div class="brand"><span class="brand-dot"></span>PETER LINDQVIST</div>
  <nav class="main-nav"><span class="active">Home</span><span>About Us</span><span>Reviews</span><span>Service</span></nav>
  <span class="btn">CONTACT US</span>
</header>

<section class="about">
  <div class="ph about-portrait" role="img" aria-label="Portrait photo of the practitioner outdoors"></div>
  <div class="ph about-side" role="img" aria-label="Black and white photo of plants and foliage"></div>
  <div class="about-text">
    <span class="section-label">About Us</span>
    <h3>A Gentle Presence In Support Of Deep Inner Healing</h3>
    <p>Lorem ipsum dolor sit amet, consectetur adipiscing elit, sed do eiusmod tempor incididunt ut labore et dolore magna aliqua. Ut enim ad minim veniam, quis nostrud exercitation ullamco laboris nisi ut aliquip ex ea commodo consequat. Duis aute irure dolor in reprehenderit in voluptate velit esse cillum dolore eu fugiat.</p>
    <div class="stats">
      <div class="stat"><b>20+</b><span>Years Exprience</span></div>
      <div class="stat"><b class="gold">15</b><span>Best Award</span></div>
      <div class="stat"><b>80k+</b><span>Happy Clients</span></div>
    </div>
    <span class="btn">Learn More</span>
  </div>
</section>

<section class="services">
  <span class="section-label">Service</span>
  <h3 class="section-title">Gentle Support For Deeper Healing</h3>
  <div class="cards">
    <div class="card light">
      <svg width="26" height="26" viewBox="0 0 26 26" fill="none" stroke="#1f1a17" stroke-width="1.5"><circle cx="13" cy="13" r="11"/><circle cx="13" cy="13" r="5"/></svg>
      <h4>Somatic Awareness</h4>
      <p>Gentle, Body-Based Sessions That Help You Reconnect With Your Inner</p>
      <span class="btn">Learn More</span>
    </div>
    <div class="card">
      <svg width="26" height="26" viewBox="0 0 26 26" fill="none" stroke="#1f1a17" stroke-width="1.5"><rect x="3" y="3" width="12" height="12" rx="3"/><rect x="11" y="11" width="12" height="12" rx="3"/></svg>
      <h4>Emotional Integration</h4>
      <p>Gentle, Body-Based Sessions That Help You Reconnect With Your Inner</p>
      <span class="btn">Learn More</span>
    </div>
    <div class="card">
      <svg width="26" height="26" viewBox="0 0 26 26" fill="none" stroke="#1f1a17" stroke-width="1.5"><path d="M13 22s-9-5.5-9-11a5 5 0 0 1 9-3 5 5 0 0 1 9 3c0 5.5-9 11-9 11z"/></svg>
      <h4>Trauma-Informed Body</h4>
      <p>Gentle, Body-Based Sessions That Help You Reconnect With Your Inner</p>
      <span class="btn">Learn More</span>
    </div>
  </div>
</section>

<section class="reviews">
  <span class="section-label">Reviews</span>
  <h3 class="section-title">Gentle Reflections From Past Clients</h3>
  <div class="review-row">
    <div class="review">
      <div class="review-avatar" role="img" aria-label="Client portrait photo"></div>
      <div class="review-body">
        <div class="review-head"><b>Mira Holloway</b><span class="stars">★★★★★</span></div>
        <p>Lorem ipsum dolor sit amet, consectetur adipiscing elit, sed do eiusmod tempor incididunt ut labore et dolore magna aliqua.</p>
      </div>
    </div>
    <div class="review">
      <div class="review-avatar" role="img" aria-label="Client portrait photo"></div>
      <div class="review-body">
        <div class="review-head"><b>Mira Holloway</b><span class="stars">★★★★★</span></div>
        <p>Lorem ipsum dolor sit amet, consectetur adipiscing elit, sed do eiusmod tempor incididunt ut labore et dolore magna aliqua.</p>
      </div>
    </div>
  </div>
</section>

<section class="contact">
  <div class="contact-form">
    <div class="field">Name</div>
    <div class="field">Phone</div>
    <div class="field">Email</div>
    <div class="field">Adress</div>
    <div class="field tall">Message</div>
  </div>
  <div class="contact-info">
    <h3>Contact Us</h3>
    <h4>Let's Start The Conversation<br>Info</h4>
    <div class="info-line"><svg width="14" height="14" viewBox="0 0 24 24" fill="#1f1a17"><path d="M6.6 10.8a15 15 0 0 0 6.6 6.6l2.2-2.2a1 1 0 0 1 1-.25 11.4 11.4 0 0 0 3.6.57 1 1 0 0 1 1 1V20a1 1 0 0 1-1 1A17 17 0 0 1 3 4a1 1 0 0 1 1-1h3.5a1 1 0 0 1 1 1c0 1.25.2 2.45.57 3.57a1 1 0 0 1-.25 1z"/></svg>(238) 555-0147</div>
    <div class="info-line"><svg width="14" height="12" viewBox="0 0 24 20" fill="none" stroke="#1f1a17" stroke-width="2"><rect x="1" y="1" width="22" height="18" rx="2"/><path d="M1 3l11 8 11-8"/></svg>hello@lindqvist-mail.net</div>
    <div class="info-line"><svg width="12" height="14" viewBox="0 0 20 24" fill="#1f1a17"><path d="M10 0a8 8 0 0 0-8 8c0 6 8 16 8 16s8-10 8-16a8 8 0 0 0-8-8zm0 11a3 3 0 1 1 0-6 3 3 0 0 1 0 6z"/></svg>Ul. Lipowa Ogrodowa 12,</div>
    <div class="social">Social Media : <i></i><i></i><i></i><i></i></div>
    <span class="btn">Submit</span>
  </div>
</section>

<footer class="site-footer">
  <div class="footer-brand"><i></i>PETER LINDQVIST</div>
  <div class="footer-social"><i></i><i></i><i></i><i></i></div>
  <div class="footer-col" style="left:446px"><h5>Home</h5>About Us<br>Reviews<br>Service<br>Contact</div>
  <div class="footer-col" style="left:610px"><h5>Legal</h5>Privacy Policy<br>Terms Of Use<br>Cookie Policy</div>
  <div class="footer-note">Gentle sessions held in a quiet room near the park, open weekdays and by appointment on weekends.</div>
  <div class="footer-rule"></div>
  <div class="copyright">Copyright © 2025. All Rights Reserved.</div>
</footer>

</body>
</html>
```